Healthy Meal Delivery Website needs a new face lift

Hi there,

The current website i have is super old and outdated.

I would like a beautiful modern site that has all the same content as the previous except with a a new, modern and trustworthy feel.

The current website is http://www.fennoxdinners.ca/

Target Market(s)

Diet Meal delivery, weight loss, healthy meal delivery

Industry/Entity Type

Food Service

Number of Pages Required

5+ page

Font styles to use
Sans Serif

Requirements
Must have
• Modern & Clean
Should not have
• Anything outdated or cheesy

```html
<!DOCTYPE html>
<html lang="en">
<head>
<meta charset="utf-8">
<title>Fennox Dinners – Fresh Customized Diet Meals</title>
<link href="https://fonts.googleapis.com/css2?family=Roboto:wght@400;500;700&family=Tinos&display=swap" rel="stylesheet">
<style>
:root{
  --wood-light:#eceae6;
  --wood-mid:#dcd9d4;
  --ink:#111;
  --text:#555;
  --cyan:#29b5e0;
  --link-blue:#1f8fc7;
  --red:#d8232a;
  --olive:#4d6a1c;
  --white:#fff;
  --line:#ddd;
}
*{margin:0;padding:0;box-sizing:border-box}
html,body{width:1200px;height:2609px;overflow:hidden}
body{position:relative;font-family:'Roboto',Arial,sans-serif;color:var(--ink);background:var(--white)}
.abs{position:absolute}
.wood{background:linear-gradient(100deg,var(--wood-light) 0%,var(--wood-mid) 45%,var(--wood-light) 70%,var(--wood-mid) 100%)}
.serif{font-family:'Tinos','Times New Roman',serif;font-weight:400}
.img-fill{position:absolute}

/* top bar */
.topbar{top:10px;left:75px;right:0;height:22px;font-size:12px;display:flex;align-items:center}
.like-btn{background:#4267b2;color:#fff;font-size:10px;font-weight:700;padding:2px 6px;margin-right:3px}
.topbar .item{position:absolute;display:flex;align-items:center;gap:6px;font-size:12px}
.hamburger{position:absolute;top:12px;left:1079px;width:28px}
.hamburger span{display:block;height:3px;background:var(--ink);margin-bottom:5px}

/* nav */
.nav{top:42px;left:965px;width:148px;background:var(--cyan)}
.nav a{display:block;height:21px;line-height:21px;text-align:right;padding-right:16px;color:#fff;font-size:10.5px;font-weight:700;text-decoration:none;border-bottom:1px solid rgba(255,255,255,.45)}
.nav a.active{background:#000}

/* hero */
.hero{top:0;left:0;width:1200px;height:525px}
.logo{top:112px;left:75px;display:flex;align-items:center;gap:10px}
.logo-mark{width:26px;height:26px;background:var(--cyan);border-radius:50%}
.logo-name{font-size:40px;font-weight:700;color:var(--cyan);line-height:1}
.hero-title{top:254px;left:73px;font-size:36px;line-height:44px;letter-spacing:.3px}
.hero-sub{top:350px;left:75px;font-size:20px;color:#222}
.btn-dark{top:416px;left:75px;width:167px;height:50px;background:#000;color:#fff;font-size:14px;font-weight:500;display:flex;align-items:center;justify-content:center}

/* about */
.about{top:525px;left:0;width:1200px;height:353px;background:var(--white)}
.about-title{top:45px;left:544px;font-size:21px;line-height:27px;letter-spacing:.4px}
.rule{height:3px;width:56px;background:var(--olive)}
.about-text{top:132px;left:544px;width:585px;font-size:11.5px;line-height:18px;color:var(--text)}
.facts{top:201px;left:544px;font-size:11px;border-collapse:collapse}
.facts td{height:17px;padding:0}
.facts td:first-child{width:192px;font-weight:700;color:var(--ink)}
.facts td:last-child{color:var(--text)}

/* menu */
.menu{top:878px;left:0;width:1200px;height:722px}
.section-title{width:1200px;text-align:center;font-size:21px;line-height:26px;letter-spacing:.4px}
.tabs{top:99px;left:283px;width:634px;height:37px}
.tabs svg{position:absolute;top:0;left:0}
.tabs ul{position:absolute;top:0;left:0;width:634px;height:37px;list-style:none;display:flex;justify-content:center;gap:0;align-items:center}
.tabs li{color:#fff;font-size:12px;font-weight:700;padding:0 23px}
.tabs li.active{color:var(--cyan)}
.card{width:230px;height:223px;background:#fff;border:1px solid var(--line)}
.card .photo{left:0;top:0;width:228px;height:150px}
.card .name{position:absolute;left:16px;top:155px;font-size:11.5px;font-weight:700;line-height:14px;color:var(--ink)}
.card .price{position:absolute;left:16px;top:195px;font-size:16px;font-weight:500;color:var(--link-blue)}
.card svg{position:absolute;right:16px;top:192px}
.pager{top:675px;left:974px;font-size:13px;font-weight:700}

/* testimonials */
.testi{top:1600px;left:0;width:1200px;height:417px;background:var(--white)}
.quote{width:400px}
.quote .photo{left:0;top:0;width:174px;height:187px}
.quote .body{position:absolute;left:193px;top:0;width:300px}
.q-mark{font-family:'Tinos',serif;font-size:34px;line-height:28px;color:#333}
.q-head{font-size:12px;color:var(--link-blue);font-weight:500;margin-top:6px}
.q-text{font-size:11.5px;line-height:20px;color:var(--text);margin-top:18px}
.q-name{font-size:12px;color:var(--link-blue);font-weight:500;margin-top:20px}
.q-role{font-size:11.5px;color:var(--text);margin-top:5px}
.read-more{top:382px;left:1047px;font-size:12px;font-weight:700}

/* lower */
.lower{top:2017px;left:0;width:1200px;height:592px}
.block-title{font-size:21px;letter-spacing:.4px}
.panel{background:#fff;width:511px;height:223px}
.prog-title{position:absolute;left:193px;top:35px;font-size:12px;color:var(--link-blue);font-weight:500}
.prog-text{position:absolute;left:193px;top:66px;width:290px;font-size:11.5px;line-height:20px;color:var(--text)}
.btn-red{position:absolute;width:90px;height:29px;background:var(--red);color:#fff;font-size:12px;font-weight:500;display:flex;align-items:center;justify-content:center}
.acc{position:absolute;left:10px;width:491px}
.acc-row{height:29px;border-bottom:1px solid var(--line);display:flex;align-items:center;justify-content:space-between;padding:0 12px;font-size:11.5px;color:var(--link-blue);font-weight:500}
.acc-row.open{background:var(--cyan);color:#fff;height:25px;border:none}
.acc-body{font-size:11.5px;line-height:18px;color:var(--text);padding:5px 12px 8px;border-bottom:1px solid var(--line)}
.contact-band{top:343px;left:75px;width:1050px;height:96px;background:var(--cyan)}
.contact-band .inner{position:absolute;inset:8px;border:1px dashed rgba(255,255,255,.8)}
.contact-icon{position:absolute;left:44px;top:20px}
.contact-text{position:absolute;left:140px;top:30px;color:#fff;font-size:25px;font-weight:500}
.foot-links{top:459px;left:0;width:1200px;display:flex;justify-content:center;font-size:11px;font-weight:500}
.foot-links span{padding:0 16px;border-right:1px solid #333;line-height:12px}
.foot-links span:last-child{border:none}
.social{top:496px;left:0;width:1200px;display:flex;justify-content:center;gap:6px}
.social i{display:block;width:22px;height:22px;border-radius:50%;background:var(--link-blue)}
.copyright{top:533px;left:0;width:1200px;text-align:center;font-size:10.5px}
</style>
</head>
<body>

<!-- HERO -->
<section class="abs hero wood">
  <div class="img-fill" role="img" aria-label="Stuffed bell peppers on a dark plate with fresh herbs" style="left:574px;top:30px;width:574px;height:495px;border-radius:290px 290px 0 0;background:radial-gradient(circle at 50% 55%,#c5472a 0%,#d6a32a 30%,#3d5d22 50%,#121212 62%,rgba(18,18,18,0) 64%)"></div>

  <div class="abs topbar">
    <span class="like-btn">Like</span><span class="like-btn">Share</span>
    <span style="margin-left:4px">1.1K people like this what your friends like</span>
    <div class="item" style="left:380px">
      <svg width="22" height="18" viewBox="0 0 22 18"><path d="M1 2h3l3 10h11l2-7H6" fill="none" stroke="#111" stroke-width="2"/><circle cx="8" cy="16" r="1.6"/><circle cx="17" cy="16" r="1.6"/></svg>
      <span><b>(0)</b> Items in your Cart</span>
    </div>
    <div class="item" style="left:550px">
      <svg width="20" height="16" viewBox="0 0 20 16"><rect x="1" y="1" width="18" height="14" fill="none" stroke="#111" stroke-width="2"/><path d="M1 1l9 8 9-8" fill="none" stroke="#111" stroke-width="2"/></svg>
      <span>hello@fennoxdinners.ca</span>
    </div>
    <div class="item" style="left:767px">
      <svg width="14" height="16" viewBox="0 0 14 16"><path d="M3 1l3 4-2 2c1 2 3 4 5 5l2-2 3 3-2 3C6 15 0 9 1 3z" fill="#111"/></svg>
      <span>416-555-0142</span>
    </div>
  </div>
  <div class="hamburger"><span></span><span></span><span></span></div>

  <nav class="abs nav">
    <a class="active">HOME</a><a>HOW IT WORKS</a><a>PRICING ▾</a><a>SAMPLE MENU</a><a>CELEBRITY</a><a>F.A.Q</a><a>CONTACT</a><a>SIGN UP</a><a>CUSTOMER LOGIN</a>
  </nav>

  <div class="abs logo"><span class="logo-mark"></span><span class="logo-name">Fennox Dinners</span></div>
  <h1 class="abs hero-title serif">FRESH CUSTOMIZED DIET<br>MEALS DELIVERED DAILY</h1>
  <p class="abs hero-sub">Providing Toronto diet meal delivery for 15 years.</p>
  <div class="abs btn-dark">View Recipes</div>
</section>

<!-- ABOUT -->
<section class="abs about">
  <div class="img-fill" role="img" aria-label="Bowl of roasted mushrooms on a floral napkin with a red napkin and cutlery" style="left:75px;top:23px;width:438px;height:295px;background:linear-gradient(120deg,#d9c6b8 0%,#a98d6c 45%,#c4b4a6 70%,#b8202a 85%,#e9e2da 100%)"></div>
  <h2 class="abs about-title serif">FRESH DIET GOURMET MEALS<br>DELIVERED BY THE FENNOX</h2>
  <div class="abs rule" style="top:111px;left:544px"></div>
  <p class="abs about-text">Fresh diet meal delivery Toronto and Canada wide is our signature fresh gourmet diet meal delivery program designed for healthy living &amp; weight loss management.Diet meal delivery Toronto has a creative gourmet menu that uses exotic flavors and ingredients to enhance your dining experience.</p>
  <table class="abs facts">
    <tr><td>BENEFITS</td><td>: Fresh diet meal delivery daily</td></tr>
    <tr><td>MENU</td><td>: Inspired fresh gourmet Fennox Diet meals</td></tr>
    <tr><td>VARIETY</td><td>: 60 Day Menu Rotation</td></tr>
    <tr><td>CUSTOMIZATION</td><td>: Every fresh Fennox Diet meal is personally customized</td></tr>
    <tr><td>DELIVERY</td><td>: Fresh diet meal delivery daily Toronto and Canada wide</td></tr>
    <tr><td>CUSTOMER SERVICE</td><td>: Personal Nutritionist available 7 days a week</td></tr>
  </table>
</section>

<!-- SAMPLE MENU -->
<section class="abs menu wood">
  <h2 class="abs section-title serif" style="top:29px">SAMPLE MENU<br>FENNOX DIET MEALS</h2>
  <div class="abs rule" style="top:88px;left:572px"></div>
  <div class="abs tabs">
    <svg width="634" height="37" viewBox="0 0 634 37"><polygon points="0,0 634,0 614,18.5 634,37 0,37 20,18.5" fill="#000"/></svg>
    <ul><li class="active">Breakfast</li><li>Lunch</li><li>Afternoon Snack</li><li>Evening Snacks</li><li>Dinner</li></ul>
  </div>

  <div class="abs card" style="left:115px;top:181px"><div class="img-fill photo" role="img" aria-label="Egg white omelette with fruit salad" style="background:linear-gradient(135deg,#6f8f4a,#e6c04a,#f0ead2)"></div><p class="name">Eggwhite and Asparagus Omelette<br>with fresh fruit salad</p><p class="price">$05.00</p><svg width="22" height="20" viewBox="0 0 22 20"><path d="M1 2h3l3 10h11l2-7H6" fill="none" stroke="#111" stroke-width="2"/><circle cx="8" cy="17" r="1.8"/><circle cx="17" cy="17" r="1.8"/></svg></div>
  <div class="abs card" style="left:362px;top:181px"><div class="img-fill photo" role="img" aria-label="Pear and camembert crepes" style="background:linear-gradient(135deg,#3a2a1e,#8a6a3e,#e8e0d0)"></div><p class="name">Pear and Camembert<br>Crepes</p><p class="price">$06.00</p><svg width="22" height="20" viewBox="0 0 22 20"><path d="M1 2h3l3 10h11l2-7H6" fill="none" stroke="#111" stroke-width="2"/><circle cx="8" cy="17" r="1.8"/><circle cx="17" cy="17" r="1.8"/></svg></div>
  <div class="abs card" style="left:609px;top:181px"><div class="img-fill photo" role="img" aria-label="Glazed salmon with asparagus" style="background:linear-gradient(135deg,#2e3e22,#b0542a,#6b3a1e)"></div><p class="name">Clara Bell's<br>Personal Gourmet</p><p class="price">$07.00</p><svg width="22" height="20" viewBox="0 0 22 20"><path d="M1 2h3l3 10h11l2-7H6" fill="none" stroke="#111" stroke-width="2"/><circle cx="8" cy="17" r="1.8"/><circle cx="17" cy="17" r="1.8"/></svg></div>
  <div class="abs card" style="left:856px;top:181px"><div class="img-fill photo" role="img" aria-label="Western egg sandwich on a bun" style="background:linear-gradient(160deg,#e8e4dc,#c88a42,#d9b25a)"></div><p class="name">Western Sandwich<br>Full Plate</p><p class="price">$04.00</p><svg width="22" height="20" viewBox="0 0 22 20"><path d="M1 2h3l3 10h11l2-7H6" fill="none" stroke="#111" stroke-width="2"/><circle cx="8" cy="17" r="1.8"/><circle cx="17" cy="17" r="1.8"/></svg></div>

  <div class="abs card" style="left:115px;top:430px"><div class="img-fill photo" role="img" aria-label="Peameal bacon sandwich with coleslaw" style="background:linear-gradient(160deg,#b5713a,#8a3a4a,#d9a45a)"></div><p class="name">Peameal<br>Bacon Sandwich</p><p class="price">$10.00</p><svg width="22" height="20" viewBox="0 0 22 20"><path d="M1 2h3l3 10h11l2-7H6" fill="none" stroke="#111" stroke-width="2"/><circle cx="8" cy="17" r="1.8"/><circle cx="17" cy="17" r="1.8"/></svg></div>
  <div class="abs card" style="left:362px;top:430px"><div class="img-fill photo" role="img" aria-label="Grilled cheese with fries" style="background:linear-gradient(160deg,#f2f0ea,#e8b640,#d0902a)"></div><p class="name">Kids Grilled<br>Cheese</p><p class="price">$05.00</p><svg width="22" height="20" viewBox="0 0 22 20"><path d="M1 2h3l3 10h11l2-7H6" fill="none" stroke="#111" stroke-width="2"/><circle cx="8" cy="17" r="1.8"/><circle cx="17" cy="17" r="1.8"/></svg></div>
  <div class="abs card" style="left:609px;top:430px"><div class="img-fill photo" role="img" aria-label="Plate of potato latkes" style="background:linear-gradient(160deg,#1e3a44,#b8672a,#8a4a1e)"></div><p class="name">Potato Latkes<br>Full Plate</p><p class="price">$03.00</p><svg width="22" height="20" viewBox="0 0 22 20"><path d="M1 2h3l3 10h11l2-7H6" fill="none" stroke="#111" stroke-width="2"/><circle cx="8" cy="17" r="1.8"/><circle cx="17" cy="17" r="1.8"/></svg></div>
  <div class="abs card" style="left:856px;top:430px"><div class="img-fill photo" role="img" aria-label="French toast platter with eggs" style="background:linear-gradient(160deg,#6a3a24,#e8e2d8,#b06a2e)"></div><p class="name">French Toast<br>Platter</p><p class="price">$06.00</p><svg width="22" height="20" viewBox="0 0 22 20"><path d="M1 2h3l3 10h11l2-7H6" fill="none" stroke="#111" stroke-width="2"/><circle cx="8" cy="17" r="1.8"/><circle cx="17" cy="17" r="1.8"/></svg></div>

  <p class="abs pager">Previous &nbsp;&nbsp;|&nbsp;&nbsp; Next</p>
</section>

<!-- TESTIMONIALS -->
<section class="abs testi">
  <h2 class="abs section-title serif" style="top:36px">CELEBRITY TESTIMONIALS FENNOX<br>DIET MEAL DELIVERY</h2>
  <div class="abs rule" style="top:97px;left:572px"></div>

  <div class="abs quote" style="left:155px;top:149px">
    <div class="img-fill photo" role="img" aria-label="Actress seated at a dining table" style="background:linear-gradient(135deg,#6b5a4a,#a8948a,#3e3a36)"></div>
    <div class="body">
      <div class="q-mark">“</div>
      <p class="q-head">Tasty &amp; Healthy</p>
      <p class="q-text">The Fennox Diet is simple and it works!<br>I am so greatful to have used the Fennox Diet.<br>So tasty and so healthy.</p>
      <p class="q-name">Maren Holt</p>
      <p class="q-role">Actress</p>
    </div>
  </div>

  <div class="abs quote" style="left:643px;top:149px">
    <div class="img-fill photo" role="img" aria-label="Actor dining at a restaurant" style="background:linear-gradient(135deg,#3a2a22,#9a6a4a,#e0d6c8)"></div>
    <div class="body">
      <div class="q-mark">“</div>
      <p class="q-head">Fresh &amp; Delicious</p>
      <p class="q-text">When in Toronto filming I know I can depend<br>on FennoxDinners.ca for fresh, delicious meals delivered<br>daily, fabulous, easy and convenient.</p>
      <p class="q-name">Tobias Crane</p>
      <p class="q-role">Actress</p>
    </div>
  </div>

  <p class="abs read-more">Read More</p>
</section>

<!-- PROGRAM / DELIVERY -->
<section class="abs lower wood">
  <h3 class="abs block-title serif" style="top:58px;left:75px">PROGRAM DETAILS</h3>
  <h3 class="abs block-title serif" style="top:61px;left:614px">DELIVERY SYSTEM</h3>

  <div class="abs panel" style="top:99px;left:75px">
    <div class="img-fill" role="img" aria-label="Vegetable wrap cut in halves" style="left:21px;top:25px;width:161px;height:144px;background:linear-gradient(135deg,#d8c8a8,#b8562a,#6a8a3a,#e8dcc0)"></div>
    <p class="prog-title">PAUSE YOUR PROGRAM ANYTIME</p>
    <p class="prog-text">You are welcome to pause and restart your meal program at anytime. Our customers lead busy lives, therefore if you need to post-pone a delivery let us know with at least 48 Hours notice prior to your delivery.</p>
    <div class="btn-red" style="left:398px;top:178px">Order Now</div>
  </div>

  <div class="abs panel" style="top:99px;left:614px">
    <div class="acc" style="top:12px">
      <div class="acc-row open"><span>WHAT'S IN YOUR BAG?</span><span>−</span></div>
      <div class="acc-body">Your daily temperature controlled cooler will have all of your meals so you won't need to supplement with any additional snacks or produce during the day.</div>
      <div class="acc-row"><span>YOUR DAILY MENU</span><span style="color:#333">+</span></div>
      <div class="acc-row"><span>RECYCLABLE CONTAINERS</span><span style="color:#333">+</span></div>
      <div class="acc-row"><span>RETURNING YOUR COOLER</span><span style="color:#333">+</span></div>
    </div>
    <div class="btn-red" style="left:405px;top:178px">Order Now</div>
  </div>

  <div class="abs contact-band">
    <div class="inner"></div>
    <svg class="contact-icon" width="60" height="60" viewBox="0 0 60 60"><circle cx="30" cy="30" r="27" fill="none" stroke="#fff" stroke-width="3"/><path d="M15 22h30v18H15z M15 22l15 11 15-11" fill="none" stroke="#fff" stroke-width="3" stroke-linejoin="round"/></svg>
    <p class="contact-text">Still have questions? Contact Us now at: hello@fennoxdinners.ca</p>
  </div>

  <div class="abs foot-links"><span>HOME</span><span>HOW IT WORKS</span><span>PRICING</span><span>SIGN UP</span><span>CONTACT US</span><span>TERMS OF USE</span></div>
  <div class="abs social"><i></i><i></i><i></i><i></i><i></i><i></i><i></i><i></i></div>
  <p class="abs copyright">Copyright 2018, fennoxdinners.ca.All Rights Reserved</p>
</section>

</body>
</html>
```